Sticker Design Project

I want a design for my new synthetic 10W/50 motor oil.
It will be of international standard since it will be offered in several countries.
We are a lubricant manufacturing and marketing company operating in several African countries.

Target Market(s)

Top range car owners and garages

Industry/Entity Type

Marketing

Requirements
Must have
• images related to autos

```html
<!DOCTYPE html>
<html lang="en">
<head>
<meta charset="utf-8">
<title>Kestrel Prime 10W/50 Sticker Labels</title>
<link href="https://fonts.googleapis.com/css2?family=Archivo+Black&family=Archivo:wght@700;800&display=swap" rel="stylesheet">
<style>
  :root{
    --canvas:#ffffff;
    --blue-deep:#0a3c96;
    --blue-mid:#1466c8;
    --blue-light:#3aa6ee;
    --cyan:#43d2f7;
    --yellow:#ffe81a;
    --yellow-dark:#f2b705;
    --red:#c5121b;
    --red-dark:#8e0a10;
    --orange:#ff7a12;
    --white:#ffffff;
    --engine-a:#1a6fc4;
    --engine-b:#0d3f86;
  }
  *{margin:0;padding:0;box-sizing:border-box}
  html,body{width:1200px;height:1000px;overflow:hidden;background:var(--canvas)}
  body{position:relative;font-family:"Archivo Black","Archivo",sans-serif}

  .label{position:absolute;overflow:hidden;border-radius:22px;
    background:linear-gradient(160deg,var(--blue-light) 0%,var(--blue-mid) 40%,var(--blue-deep) 100%);
    box-shadow:0 10px 30px rgba(0,0,0,.18)}
  .label svg.art{position:absolute;inset:0;width:100%;height:100%}
  .label .txt{position:absolute;white-space:nowrap;line-height:1}

  .brand{display:flex;align-items:center;gap:10px}
  .brand-dot{width:36px;height:36px;border-radius:50%;background:var(--yellow)}
  .brand-name{font-family:"Archivo Black",sans-serif;color:var(--yellow);font-size:24px;line-height:1.05}

  .line-synthetic{color:var(--white);letter-spacing:2px}
  .grade{color:var(--yellow);text-shadow:3px 3px 0 var(--blue-deep)}
  .motor-oil{color:var(--cyan);text-align:center}
  .performance{color:var(--white);font-family:"Archivo",sans-serif;font-weight:800;line-height:1.02}
  .volume{color:var(--white);font-family:"Archivo",sans-serif;font-weight:700}

  /* pail label */
  .label--pail{left:50px;top:300px;width:640px;height:400px}
  .label--pail .brand{left:24px;top:36px}
  .label--pail .line-synthetic{left:45px;top:158px;font-size:34px}
  .label--pail .grade{left:38px;top:190px;font-size:100px}
  .label--pail .motor-oil{left:448px;top:128px;font-size:36px;line-height:1}
  .label--pail .performance{left:175px;top:344px;font-size:21px}
  .label--pail .volume{left:392px;top:372px;font-size:16px}

  /* jug label */
  .label--jug{left:790px;top:255px;width:300px;height:495px;border-radius:34px 34px 18px 18px}
  .label--jug .brand{left:0;right:0;top:44px;flex-direction:column;gap:8px;text-align:center}
  .label--jug .brand-name{font-size:26px}
  .label--jug .line-synthetic{left:16px;top:222px;font-size:24px}
  .label--jug .grade{left:14px;top:256px;font-size:68px}
  .label--jug .motor-oil{left:126px;top:324px;font-size:26px}
  .label--jug .performance{left:10px;top:410px;font-size:17px}
  .label--jug .volume{left:16px;top:470px;font-size:13px}
</style>
</head>
<body>

<section class="label label--pail" aria-label="18 litre pail sticker">
  <svg class="art" viewBox="0 0 640 400" preserveAspectRatio="none">
    <polygon points="0,0 640,0 640,40 0,150" fill="#5bbdf5" opacity=".55"/>
    <polygon points="0,150 640,40 640,95 0,215" fill="#0b4eb0" opacity=".35"/>
    <g role="img" aria-label="Blue-toned engine illustration">
      <polygon points="380,312 640,275 640,400 352,400" fill="url(#engPail)"/>
    </g>
    <polygon points="0,340 640,255 640,273 0,358" fill="var(--yellow)"/>
    <polygon points="0,358 640,273 640,277 0,362" fill="var(--yellow-dark)"/>
    <polygon points="0,362 380,312 352,400 0,400" fill="url(#redPail)"/>
    <g fill="var(--orange)">
      <rect x="290" y="326" width="6" height="18"/><rect x="302" y="325" width="6" height="18"/>
      <rect x="314" y="323" width="6" height="18"/><rect x="326" y="321" width="6" height="18"/>
      <rect x="338" y="320" width="6" height="18"/><rect x="350" y="318" width="6" height="18"/>
    </g>
    <defs>
      <linearGradient id="engPail" x1="0" y1="0" x2="1" y2="1">
        <stop offset="0" stop-color="var(--engine-a)"/><stop offset="1" stop-color="var(--engine-b)"/>
      </linearGradient>
      <linearGradient id="redPail" x1="0" y1="0" x2="0" y2="1">
        <stop offset="0" stop-color="var(--red)"/><stop offset="1" stop-color="var(--red-dark)"/>
      </linearGradient>
    </defs>
  </svg>
  <div class="txt brand"><span class="brand-dot"></span><span class="brand-name">Kestrel Prime</span></div>
  <div class="txt line-synthetic">New Synthetic</div>
  <div class="txt grade">10W/50</div>
  <div class="txt motor-oil">MOTOR<br>OIL</div>
  <div class="txt performance">HIGH<br>PERFORMANCE</div>
  <div class="txt volume">18 Liters</div>
</section>

<section class="label label--jug" aria-label="5 litre jug sticker">
  <svg class="art" viewBox="0 0 300 495" preserveAspectRatio="none">
    <polygon points="0,0 300,0 300,120 0,200" fill="#5bbdf5" opacity=".5"/>
    <g role="img" aria-label="Blue-toned engine illustration">
      <polygon points="180,400 300,372 300,495 170,495" fill="url(#engJug)"/>
    </g>
    <polygon points="0,388 300,356 300,370 0,402" fill="var(--yellow)"/>
    <polygon points="0,404 215,378 205,450 0,462" fill="url(#redJug)"/>
    <g fill="var(--orange)">
      <rect x="150" y="388" width="5" height="14"/><rect x="160" y="387" width="5" height="14"/>
      <rect x="170" y="386" width="5" height="14"/><rect x="180" y="385" width="5" height="14"/>
      <rect x="190" y="384" width="5" height="14"/>
    </g>
    <defs>
      <linearGradient id="engJug" x1="0" y1="0" x2="1" y2="1">
        <stop offset="0" stop-color="var(--engine-a)"/><stop offset="1" stop-color="var(--engine-b)"/>
      </linearGradient>
      <linearGradient id="redJug" x1="0" y1="0" x2="0" y2="1">
        <stop offset="0" stop-color="var(--red)"/><stop offset="1" stop-color="var(--red-dark)"/>
      </linearGradient>
    </defs>
  </svg>
  <div class="txt brand"><span class="brand-dot"></span><span class="brand-name">Kestrel Prime</span></div>
  <div class="txt line-synthetic">New Synthetic</div>
  <div class="txt grade">10W/50</div>
  <div class="txt motor-oil">MOTOR OIL</div>
  <div class="txt performance">HIGH<br>PERFORMANCE</div>
  <div class="txt volume">5 Liters</div>
</section>

</body>
</html>
```